Diesel injection diagnostics and repairs

I am after a business card design for my business.
The business; repairs diesel fuel systems on 4wds, trucks, earthmoving equipment,can do mobile repairs and diagnostics
The business design can basic but effective, I guess some colours such as green and black or even blue......
The end result should reflect the business name and logo and what the business can do

Industry/Entity Type

Business

Contact Information for Business Card

BW Diesel Injection PTY LTD
bw_diesel@trovamail.net
Dennis Holt
0491570156

```html
<!DOCTYPE html>
<html lang="en">
<head>
<meta charset="utf-8">
<title>BW Diesel Injection – Business Card</title>
<link rel="stylesheet" href="https://fonts.googleapis.com/css2?family=Anton&family=Arimo&family=Montserrat:wght@600&display=swap">
<style>
  :root {
    --page-bg: #e6e7e8;
    --card-white: #ffffff;
    --card-border: #9a9a9a;
    --band-black: #000000;
    --accent-yellow: #fff200;
    --text-dark: #111111;
    --icon-white: #ffffff;
  }
  html, body {
    margin: 0;
    padding: 0;
    width: 931px;
    height: 1200px;
    overflow: hidden;
    background: var(--page-bg);
  }
  .canvas {
    position: relative;
    width: 931px;
    height: 1200px;
  }
  .card {
    position: absolute;
    left: 112px;
    width: 713px;
    height: 435px;
    box-sizing: border-box;
    overflow: hidden;
  }
  .card--front {
    top: 110px;
    border: 1px solid #6d6d6d;
  }
  .injector-photo {
    position: absolute;
    inset: 0;
    background:
      radial-gradient(ellipse 18% 14% at 68% 24%, #b8b2ae 0%, #6c6460 40%, transparent 100%),
      radial-gradient(ellipse 70% 55% at 62% 30%, #4a403d 0%, #231c1b 50%, #0d0909 100%);
  }
  .logo-band {
    position: absolute;
    left: 87px;
    top: 208px;
    width: 626px;
    height: 154px;
    background: var(--band-black);
    display: flex;
    align-items: center;
    padding-left: 36px;
    box-sizing: border-box;
  }
  .brand-name {
    font-family: "Anton", sans-serif;
    font-size: 56px;
    line-height: 1;
    color: var(--accent-yellow);
    letter-spacing: 1px;
    margin: 0;
    font-weight: 400;
  }
  .card--back {
    top: 604px;
    height: 437px;
    background: var(--card-white);
    border: 1px solid var(--card-border);
  }
  .person-name {
    position: absolute;
    left: 72px;
    top: 172px;
    margin: 0;
    font-family: "Montserrat", sans-serif;
    font-weight: 600;
    font-size: 37px;
    color: var(--text-dark);
  }
  .contact-band {
    position: absolute;
    left: 0;
    top: 222px;
    width: 585px;
    height: 154px;
    background: var(--band-black);
  }
  .contact-list {
    list-style: none;
    margin: 0;
    padding: 0;
    position: absolute;
    left: 72px;
    top: 42px;
  }
  .contact-item {
    display: flex;
    align-items: center;
    height: 40px;
    font-family: "Arimo", sans-serif;
    font-size: 28px;
    color: var(--accent-yellow);
  }
  .contact-icon {
    width: 30px;
    height: 30px;
    margin-right: 22px;
    flex: none;
  }
</style>
</head>
<body>
<div class="canvas">
  <section class="card card--front">
    <div class="injector-photo" role="img" aria-label="Close-up photograph of a diesel injector nozzle spraying fuel on a dark background"></div>
    <div class="logo-band">
      <h1 class="brand-name">BW Diesel Injection</h1>
    </div>
  </section>

  <section class="card card--back">
    <h2 class="person-name">Dennis Holt</h2>
    <div class="contact-band">
      <ul class="contact-list">
        <li class="contact-item">
          <svg class="contact-icon" viewBox="0 0 30 30" aria-hidden="true">
            <path d="M3 10 C3 5 27 5 27 10 L27 13 L21 13 L21 10 L9 10 L9 13 L3 13 Z" fill="var(--icon-white)"/>
            <path d="M8 14 L22 14 L26 24 L4 24 Z" fill="var(--icon-white)"/>
            <circle cx="15" cy="19" r="3" fill="var(--band-black)"/>
          </svg>
          <span>0491570156</span>
        </li>
        <li class="contact-item">
          <svg class="contact-icon" viewBox="0 0 30 30" aria-hidden="true">
            <circle cx="13" cy="15" r="10" fill="var(--icon-white)"/>
          </svg>
          <span>bw_diesel@trovamail.net</span>
        </li>
      </ul>
    </div>
  </section>
</div>
</body>
</html>
```